Foodcard Package Design for 10ml Food Enhancer

I have developed a product with a friend that we will be selling later this year, it is a liquid that comes in a small 10ml or 20ml bottle for sale in shops (a flavour enhancer).

A small cardboard sized backer of approximate size "A5" is the best packaging for this product.

i have attached an example of what I am looking for - the front will hold the bottle inside a small plastic case, and the back will be how to use the product / instructions.

What I am looking for is:
Strong graphic design skills to capture customers attention
Good layout of "how to use" instructions so it is clear for customer to understand
Similar "feel" to attached document as guide only

(Note: I will add the words myself, the graphics is all I need. When you design the front & back you will add Lorem ipsom text to display position of text only).

Target Market(s)

Retail & Restaurant industry

Industry/Entity Type

Retail

Font styles to use
Serif

Requirements
Must have
• Captures customers attention, high impact, sophisticated
Nice to have
• Colour, cutting edge look
Should not have
• Not cheap looking

```html
<!DOCTYPE html>
<html lang="en">
<head>
<meta charset="utf-8">
<title>The Lost Flavour Thread – Backer Card</title>
<link rel="stylesheet" href="https://fonts.googleapis.com/css2?family=Cinzel:wght@400;500&family=Jost:wght@300;400&display=swap">
<style>
  :root {
    --page: #ffffff;
    --ink: #1d1d1d;
    --card-edge: #222222;
    --rule: #2a2a2a;
    --white: #ffffff;
    --wood-dark: #4a2a18;
    --wood-mid: #7a4a2c;
    --chili: #b32a1c;
    --turmeric: #e39a2a;
    --sage: #8a9a7c;
  }
  * { box-sizing: border-box; margin: 0; padding: 0; }
  html, body { width: 1200px; height: 895px; overflow: hidden; background: var(--page); }
  .sheet { position: relative; width: 1200px; height: 895px; }

  .card {
    position: absolute; top: 51px; width: 451px; height: 798px;
    border-radius: 32px; overflow: hidden;
  }
  .card--front { left: 116px; border: 2px solid var(--card-edge); }
  .card--back { left: 626px; border: 2px solid var(--card-edge); background: var(--white); }

  .front-photo {
    position: absolute; inset: 0;
    background:
      radial-gradient(circle at 10% 12%, var(--chili) 0 16%, transparent 30%),
      radial-gradient(circle at 92% 6%, var(--sage) 0 9%, transparent 18%),
      radial-gradient(circle at 88% 63%, var(--turmeric) 0 12%, transparent 22%),
      radial-gradient(circle at 8% 55%, #a32418 0 8%, transparent 18%),
      radial-gradient(circle at 10% 90%, #8c8a60 0 12%, transparent 22%),
      radial-gradient(circle at 55% 95%, #2c2f3c 0 12%, transparent 22%),
      radial-gradient(circle at 90% 90%, #3a2014 0 12%, transparent 22%),
      linear-gradient(90deg, var(--wood-dark), var(--wood-mid) 50%, var(--wood-dark));
  }

  .hang-tab { position: absolute; left: 176px; top: 38px; }

  .title {
    position: absolute; left: 0; right: 0; top: 78px;
    font-family: "Cinzel", serif; font-weight: 500;
    font-size: 38px; line-height: 36px; text-align: center; letter-spacing: 0.5px;
  }
  .card--front .title { color: var(--white); text-shadow: 0 2px 6px rgba(0,0,0,.6); }
  .card--back .title { color: var(--ink); text-shadow: 2px 3px 3px rgba(0,0,0,.35); }

  .tagline {
    position: absolute; left: 0; right: 0; top: 160px;
    font-family: "Jost", sans-serif; font-weight: 400; font-size: 16.5px; line-height: 21px;
    color: var(--white); text-align: center; letter-spacing: -0.3px;
    text-shadow: 0 1px 4px rgba(0,0,0,.7);
  }

  .blister {
    position: absolute; left: 175px; top: 220px; width: 100px; height: 540px;
    border-radius: 29px; background: rgba(240,236,232,.62);
    border: 1px solid rgba(255,255,255,.5);
  }

  .title-rule { position: absolute; left: 52px; width: 348px; top: 168px; border-top: 1.5px solid var(--rule); }
  .divider { position: absolute; left: 42px; width: 368px; border-top: 1.5px solid var(--rule); }

  .usage {
    position: absolute; left: 20px; right: 20px; text-align: center;
    font-family: "Jost", sans-serif; font-weight: 300; font-size: 17.5px; line-height: 21px; color: var(--ink);
  }
  .usage__heading { font-weight: 300; }
</style>
</head>
<body>
<main class="sheet">

  <section class="card card--front">
    <div class="front-photo" role="img" aria-label="Photo of spices in bowls on a wooden table: chili powder, dried red chilies, peppercorns, coriander seeds, turmeric, cloves, juniper berries, garlic and herbs"></div>
    <svg class="hang-tab" width="96" height="22" viewBox="0 0 96 22" aria-hidden="true">
      <path d="M10 6 H38 Q48 -2 58 6 H86 A9 9 0 0 1 86 22 H10 A9 9 0 0 1 10 6 Z" fill="#ffffff"/>
    </svg>
    <h1 class="title">THE LOST<br>FLAVOUR THREAD</h1>
    <p class="tagline">ADD TO BOILING WATER<br>FOR FARMHOUSE STYLE VEGETABLES</p>
    <div class="blister"></div>
  </section>

  <section class="card card--back">
    <svg class="hang-tab" width="98" height="32" viewBox="0 0 98 32" aria-hidden="true" style="left:176px;top:28px">
      <path d="M12 14 H36 Q49 0 62 14 H86 A8 8 0 0 1 86 30 H12 A8 8 0 0 1 12 14 Z" fill="none" stroke="#222" stroke-width="1.5"/>
    </svg>
    <h1 class="title">THE LOST<br>FLAVOUR THREAD</h1>
    <div class="title-rule"></div>

    <div class="usage" style="top:188px">
      <p class="usage__heading">MASHED POTATOES</p>
      <p>Add wooded earth and charm to mashed<br>potatoes.<br>Can be used in place of cream &amp; butter.</p>
      <p>&nbsp;</p>
      <p>Add 2 drops to your bowl of mashed potatoes<br>for an earth charm flavour.</p>
    </div>
    <div class="divider" style="top:344px"></div>

    <div class="usage" style="top:356px">
      <p class="usage__heading">RICE</p>
      <p>Or apply to boiled rice for a smoky plume”<br>Once rice is cooked stir in 2 drops and<br>experience the difference</p>
    </div>
    <div class="divider" style="top:449px"></div>

    <div class="usage" style="top:461px">
      <p class="usage__heading">SAUCES</p>
      <p>Do you make your own sauces?<br>Stir in 2 drops to your sauces for an extra level of<br>depth.</p>
    </div>
    <div class="divider" style="top:556px"></div>

    <div class="usage" style="top:566px">
      <p class="usage__heading">STEWS CASSEROLES</p>
      <p>Add 2 drops to your bowl of mashed potatoes<br>for a smokey charm</p>
    </div>
    <div class="divider" style="top:641px"></div>

    <div class="usage" style="top:650px">
      <p class="usage__heading">PERFECT WHISKY</p>
      <p>Mix with water and freeze into ice cube trays.<br>Add cubes to torn ordinary whisky into a<br>premium aged whisky</p>
    </div>
  </section>

</main>
</body>
</html>
```